Needed Box Packaging: Dog XL Puppy Pee/Poo Pads

We're looking for a creative and fun design for our XL puppy pads. Attached is all the documents you will need.

Our pads are unique with Bamboo Charcoal and optional Adhesive sticker backing on the corners. 23" x 35" is the size. There's 50 per box.

ABSORBS 2x as much, 2x as fast, so you never come home to ruined floors
BLACK puppy pads, so your pets mess stays discrete and you never see a yellow stain on a white puppy pad in your home
ODOR ELIMINATION with carbon technology for all-day use to ensure your home stays fresh
LEAK PROOF Sorbix Polymer turns liquid into gel instantly to guarantee dry floors and easy clean up
PHEROMONE ATTRACTION to ensure pets feel comfortable and knows to hit the right spot every time

Target Market(s)

Dog owners

Font styles to use
Sans Serif

Colors
33a6d7
33b8a4
acd036
fbee3d
faa54b

Requirements
Must have
• Must have logo, size of pads, benefits, UPC code, number packed per box, pictures of a dog and picture of the pads
Should not have
• cats

```html
<!DOCTYPE html>
<html lang="en">
<head>
<meta charset="utf-8">
<title>Houndwell Bamboo Charcoal Puppy Pads – XL Box Dieline</title>
<link href="https://fonts.googleapis.com/css2?family=Open+Sans:ital,wght@0,400;0,600;0,700;0,800;1,400;1,600;1,700;1,800&display=swap" rel="stylesheet">
<style>
  :root{
    --lime:#b4cf3f;
    --lime-deep:#a3c12f;
    --teal:#52b6a2;
    --teal-deep:#3c9f8c;
    --yellow:#f3ec3e;
    --ink:#2f3a1c;
    --charcoal:#3b3b3b;
    --rule:#1b1b1b;
    --paper:#ffffff;
  }
  *{box-sizing:border-box;margin:0;padding:0}
  html,body{width:1200px;height:1200px;overflow:hidden;background:var(--paper)}
  body{font-family:"Open Sans",Arial,sans-serif;color:var(--ink)}
  .dieline{position:absolute;left:0;top:0;width:1440px;height:1440px;transform:scale(0.833333);transform-origin:0 0}
  .panel{position:absolute;overflow:hidden;background:var(--paper);border:1.5px solid var(--rule)}
  .panel > *{position:absolute}
  .flip{transform:rotate(180deg)}
  .bg{left:0;top:0;width:100%;height:100%}

  /* headline group: big 2X with stacked words and optional tagline */
  .headline-group{display:flex;align-items:flex-start;gap:6px}
  .headline-group .big{font-weight:800;font-style:italic;color:var(--teal);font-size:60px;line-height:.85;letter-spacing:-2px}
  .headline-group .stack{display:flex;flex-direction:column;padding-top:2px}
  .headline-group .small{font-weight:800;font-style:italic;color:var(--teal);font-size:21px;line-height:.92;letter-spacing:-.5px}
  .headline-group .tagline{font-weight:700;font-style:italic;font-size:12px;line-height:1.1;color:var(--charcoal);margin-top:4px;white-space:nowrap}

  .count-badge{background:var(--teal);color:#fff;font-weight:600;display:flex;align-items:center;gap:4px;padding:0 8px}
  .count-badge .num{font-size:40px;line-height:1}
  .count-badge .unit{font-size:18px;line-height:.85;font-weight:700}
  .size-mark{color:#fff;font-weight:800;font-style:italic;text-align:right}
  .size-mark .xl{font-size:44px;line-height:1;letter-spacing:-2px;display:block}
  .size-mark .dim{font-size:9px;display:block}

  .brand-block{background:var(--lime);clip-path:polygon(0 9%,100% 0,100% 86%,0 100%);color:#fff}
  .brand-name{font-weight:700;font-size:20px;color:var(--ink);display:flex;align-items:center;gap:4px}
  .brand-name .dot{width:11px;height:11px;border-radius:50%;background:var(--ink)}
  .brand-sub{font-weight:600;font-style:italic;font-size:14px;color:var(--yellow)}
  .brand-title{font-weight:600;font-size:54px;line-height:.9;letter-spacing:-1px;color:#fff}

  .photo{display:block}
  .dog-photo{background:radial-gradient(ellipse at 50% 45%,#5a4e46 0%,#2a2624 45%,#161616 70%,rgba(22,22,22,0) 72%)}
  .pad-photo{background:linear-gradient(135deg,#5a5a5a,#2c2c2c)}
  .silhouette{background:var(--yellow)}

  .callout{background:var(--yellow);color:var(--charcoal);font-size:11px;font-style:italic;font-weight:600;line-height:1.2;padding:8px}
  .callout b{font-weight:700;font-size:13px;font-style:normal;text-transform:uppercase}
  .up-read{writing-mode:vertical-rl;transform:rotate(180deg)}
  .down-read{writing-mode:vertical-rl}

  .step{width:40px;height:40px;border-radius:50%;background:var(--lime);border:3px solid #fff;box-shadow:0 0 0 1px var(--lime);color:#fff;font-weight:600;font-size:24px;display:flex;align-items:center;justify-content:center}

  .side-trim{left:0;width:100%;height:10px;background:var(--lime)}
  .side-trim.top{top:0}
  .side-trim.bottom{bottom:0}

  .benefit-icon{text-align:center;font-size:7px;font-weight:600;color:var(--charcoal);width:70px;line-height:1.1}
  .benefit-icon svg{display:block;margin:0 auto 3px}

  .layer-tag{width:56px;height:56px;border-radius:50%;background:#fff;border:2px solid var(--lime);display:flex;flex-direction:column;align-items:center;justify-content:center;text-align:center;font-size:6px;line-height:1.05;color:var(--charcoal);padding:3px}
  .layer-tag b{font-size:7px;font-weight:800}
  .layer-tag.wide{width:62px;height:62px}
</style>
</head>
<body>
<main class="dieline">

  <!-- TOP TUCK FLAP -->
  <section class="panel flip" style="left:455px;top:13px;width:538px;height:290px">
    <svg class="bg" viewBox="0 0 538 290" preserveAspectRatio="none"><polygon points="0,0 538,0 538,85 0,3" fill="var(--lime)"/></svg>
    <div class="photo dog-photo" role="img" aria-label="Photo of a black and white dog lying on its back, mouth open" style="left:340px;top:60px;width:198px;height:230px"></div>
    <div class="photo pad-photo" role="img" aria-label="Photo of a black charcoal puppy pad" style="left:203px;top:225px;width:165px;height:65px;clip-path:polygon(40% 0,100% 0,100% 100%,0 100%)"></div>
    <div class="brand-block" style="left:0;top:43px;width:193px;height:195px;padding:22px 10px 0 14px">
      <div class="brand-name">Houndwell <span class="dot"></span></div>
      <div class="brand-sub">Bamboo Charcoal</div>
      <div class="brand-title">PUPPY<br>PADS</div>
    </div>
    <div style="left:200px;top:88px;width:150px;color:var(--yellow);font-weight:700;font-style:italic;font-size:15px;line-height:1.05;transform:rotate(-6deg);text-align:center">NO MORE YELLOW<br>STAINS!</div>
    <div class="size-mark" style="left:150px;top:212px;width:70px;color:var(--teal)">
      <span class="xl">XL</span><span class="dim" style="color:var(--teal)">23"x 35" each</span>
    </div>
    <div class="count-badge" style="left:418px;top:205px;width:120px;height:62px;transform:rotate(-3deg)">
      <span class="num">50</span><span class="unit">PUPPY<br>PADS</span>
    </div>
  </section>

  <!-- LID TOP -->
  <section class="panel flip" style="left:455px;top:303px;width:538px;height:415px;background:var(--lime)">
    <div style="left:0;top:0;width:100%;height:100%;display:flex;flex-direction:column;align-items:center;justify-content:center;gap:12px">
      <div style="width:116px;height:116px;border-radius:50%;border:3px solid var(--ink)"></div>
      <div style="font-weight:700;font-size:19px;color:var(--ink)">Houndwell</div>
    </div>
  </section>

  <!-- LID SIDE LEFT -->
  <section class="panel" style="left:309px;top:303px;width:146px;height:415px">
    <div class="side-trim top"></div><div class="side-trim bottom"></div>
    <div style="left:0;top:118px;width:21px;height:105px;background:var(--yellow);clip-path:polygon(0 0,100% 100%,0 100%)"></div>
    <div class="photo" role="img" aria-label="Small dark silhouette of a dog" style="left:84px;top:75px;width:40px;height:62px;background:#4a4a4a;border-radius:30%"></div>
    <div class="callout up-read" style="left:31px;top:197px;width:95px;height:210px">
      <span><b>Pheromone Attraction</b> to ensure pets feel comfortable and knows to hit the right spot every time.</span>
    </div>
  </section>

  <!-- LID SIDE RIGHT -->
  <section class="panel" style="left:993px;top:303px;width:146px;height:415px">
    <div class="side-trim top"></div><div class="side-trim bottom"></div>
    <div class="down-read" style="left:38px;top:32px;height:150px;color:var(--yellow);font-weight:700;font-style:italic;font-size:15px;line-height:1.1">NO MORE YELLOW STAINS!</div>
    <div class="step" style="left:95px;top:194px">2</div>
    <div class="step" style="left:27px;top:237px">3</div>
    <div class="photo pad-photo" role="img" aria-label="Black puppy pad with a yellow dog silhouette on it" style="left:82px;top:242px;width:60px;height:112px;clip-path:polygon(50% 0,100% 30%,50% 100%,0 70%)"></div>
    <div class="photo silhouette" role="img" aria-label="Yellow dog silhouette" style="left:94px;top:250px;width:46px;height:52px;border-radius:35%"></div>
    <div class="photo pad-photo" role="img" aria-label="Folded black puppy pad" style="left:7px;top:287px;width:55px;height:110px;clip-path:polygon(55% 0,100% 25%,45% 100%,0 75%)"></div>
  </section>

  <!-- BACK PANEL -->
  <section class="panel flip" style="left:455px;top:718px;width:538px;height:292px">
    <div class="headline-group" style="left:33px;top:32px">
      <span class="big">2X</span>
      <span class="stack"><span class="small">FASTER</span><span class="small">ABSORPTION</span></span>
    </div>
    <div style="left:0;top:140px;width:263px;height:100px;background:linear-gradient(90deg,var(--teal) 0%,rgba(82,182,162,.55) 75%,rgba(82,182,162,0) 100%);clip-path:polygon(0 18%,100% 0,100% 82%,0 100%);padding:16px 12px 0 14px;color:#fff;font-size:13px;line-height:1.15;transform:rotate(-4deg)">
      <b style="font-weight:800;font-size:17px">SIX LAYERS</b> <i>for extra absorption and adhesive sticker backing on the corners so you'll never have to worry of any mess!</i>
    </div>
    <div class="photo" role="img" aria-label="Exploded diagram of the six pad layers over a soft teal glow" style="left:313px;top:60px;width:180px;height:180px;border-radius:50%;background:radial-gradient(circle,#ffffff 20%,#bfe9ef 55%,rgba(191,233,239,0) 72%)"></div>
    <svg style="left:303px;top:50px" width="200" height="200" viewBox="0 0 200 200">
      <defs><path id="arc" d="M20,100 A80,80 0 0 1 180,100"/></defs>
      <text font-family="Open Sans, sans-serif" font-size="9" font-weight="700" fill="var(--teal-deep)" letter-spacing="1.5"><textPath href="#arc" startOffset="50%" text-anchor="middle">6 LAYER COMPOSITION</textPath></text>
    </svg>
    <div class="layer-tag" style="left:453px;top:64px"><b>TEAR RESISTANT</b>top sheet</div>
    <div class="layer-tag wide" style="left:470px;top:121px"><b>ANTI BACTERIAL &amp; ODOR ELIMINATING</b>scented tissue</div>
    <div class="layer-tag" style="left:435px;top:192px"><b>LEAK-PROOF</b>plastic liner</div>
    <div class="layer-tag wide" style="left:252px;top:164px"><b>QUICK DRYING GEL</b>provides immediate absorption, converts liquid to gel and locks in moisture</div>
    <div class="layer-tag" style="left:255px;top:89px"><b>QUILTED</b>material draws in moisture to prevent tracking</div>
  </section>

  <!-- FRONT SIDE LEFT -->
  <section class="panel" style="left:309px;top:1010px;width:146px;height:417px">
    <div class="side-trim top"></div><div class="side-trim bottom"></div>
    <div class="callout down-read" style="left:30px;top:10px;width:100px;height:205px">
      <span><b>Odor Elimination</b> with carbon technology for all-day use to ensure your home stays fresh.</span>
    </div>
    <div class="callout down-read" style="left:4px;top:200px;width:78px;height:208px">
      <span><b>Leak Proof</b> Sorbix Polymer turns liquid into gel instantly to guarantee dry floors and easy clean up.</span>
    </div>
  </section>

  <!-- FRONT PANEL -->
  <section class="panel" style="left:455px;top:1010px;width:538px;height:417px">
    <svg class="bg" viewBox="0 0 538 417" preserveAspectRatio="none"><polygon points="0,392 538,336 538,417 0,417" fill="var(--lime)"/></svg>
    <div class="photo pad-photo" role="img" aria-label="Photo of a black charcoal puppy pad" style="left:110px;top:328px;width:210px;height:62px;clip-path:polygon(0 30%,100% 0,100% 60%,0 100%)"></div>
    <div class="photo dog-photo" role="img" aria-label="Photo of a smiling black and white dog sitting" style="left:262px;top:96px;width:276px;height:306px"></div>
    <div class="brand-block" style="left:0;top:15px;width:192px;height:192px;padding:24px 10px 0 16px">
      <div class="brand-name">Houndwell <span class="dot"></span></div>
      <div class="brand-sub">Bamboo Charcoal</div>
      <div class="brand-title">PUPPY<br>PADS</div>
    </div>
    <div class="headline-group" style="left:290px;top:22px;transform:rotate(-6deg);transform-origin:left top">
      <span class="big">2X</span>
      <span class="stack">
        <span class="small">FASTER</span><span class="small">ABSORPTION</span>
        <span class="tagline">So you never come home<br>to ruined floors!</span>
      </span>
    </div>

    <div class="benefit-icon" style="left:12px;top:218px">
      <svg width="54" height="54" viewBox="0 0 54 54"><circle cx="27" cy="27" r="24" fill="#fff" stroke="var(--lime)" stroke-width="4"/><path d="M18 38c-4-6 4-10 0-18M26 38c-4-6 4-10 0-18M34 38c-4-6 4-10 0-18" stroke="var(--charcoal)" stroke-width="3" fill="none"/><line x1="12" y1="42" x2="42" y2="12" stroke="var(--charcoal)" stroke-width="3"/></svg>
      ODOR<br>ELIMINATION
    </div>
    <div class="benefit-icon" style="left:80px;top:248px">
      <svg width="54" height="54" viewBox="0 0 54 54"><circle cx="27" cy="27" r="24" fill="#fff" stroke="var(--lime)" stroke-width="4"/><path d="M20 18c4 6 6 9 6 12a6 6 0 0 1-12 0c0-3 2-6 6-12zM34 18c4 6 6 9 6 12a6 6 0 0 1-12 0c0-3 2-6 6-12z" fill="var(--charcoal)"/><line x1="12" y1="42" x2="42" y2="12" stroke="var(--charcoal)" stroke-width="3"/></svg>
      LEAK<br>PROOF
    </div>
    <div class="benefit-icon" style="left:148px;top:218px">
      <svg width="54" height="54" viewBox="0 0 54 54"><circle cx="27" cy="27" r="24" fill="#fff" stroke="var(--lime)" stroke-width="4"/><ellipse cx="19" cy="28" rx="8" ry="9" fill="var(--charcoal)"/><ellipse cx="35" cy="28" rx="8" ry="9" fill="var(--charcoal)"/></svg>
      PHEROMONE<br>ATTRACTION
    </div>

    <div class="count-badge" style="left:4px;top:348px;width:120px;height:56px;transform:rotate(-4deg)">
      <span class="num">50</span><span class="unit">PUPPY<br>PADS</span>
    </div>
    <div class="size-mark" style="left:440px;top:348px;width:90px">
      <span class="xl">XL</span><span class="dim">23"x 35" each</span>
    </div>
  </section>

  <!-- FRONT SIDE RIGHT -->
  <section class="panel" style="left:993px;top:1010px;width:146px;height:417px">
    <div class="side-trim top"></div><div class="side-trim bottom"></div>
    <div class="photo pad-photo" role="img" aria-label="Black puppy pad with a yellow dog silhouette on it" style="left:70px;top:20px;width:70px;height:112px;clip-path:polygon(60% 0,100% 28%,45% 100%,0 72%)"></div>
    <div class="photo silhouette" role="img" aria-label="Yellow dog silhouette" style="left:72px;top:52px;width:50px;height:56px;border-radius:35%"></div>
    <div class="step" style="left:71px;top:140px">1</div>
    <div class="up-read" style="left:40px;top:195px;height:200px;font-weight:700;font-size:26px;line-height:.95;color:var(--charcoal);letter-spacing:-1px">BLACK<br>PUPPY PADS</div>
    <div class="up-read" style="left:100px;top:190px;height:205px;font-weight:700;font-style:italic;font-size:10px;line-height:1.15;color:var(--charcoal)">So your pets mess stays discrete<br>and you never see a yellow stain!</div>
  </section>

</main>
</body>
</html>
```